Keelbrook Vault Holdings Needs A Website

We are looking for a website for a new company. 4 Pages

Needs to be responsive and mobile friendly for all browsers and coded for both Android & IOS. SEO is also important.

Website Brief – Keelbrook Vault Holdings
Domain: www.keelbrookvault.net
Email: info@keelbrookvault.net
Phone: to be inserted later
Address: 40837 52 Ave, Edmonton, AB T6K 3R8
Platform: WordPress (recommended for flexibility, SEO tools, and ease of editing)
Requirements:
• Responsive & mobile-friendly (Android & iOS)
• Cross-browser compatibility
• Fast page load speed
• SEO optimized for storage development, management, and investment keywords
• Easy in-house editing after launch
• Professional, modern, trust-driven design reflecting expertise, reliability, and innovation
________________________________________
Pages
1. HOME
Purpose: Quickly communicate who Keelbrook Vault Holdings is and why they’re the best choice for designing, building, leasing, and managing self storage facilities.
Content Highlights:
• Hero Section: Large, bold image of a modern self storage facility with headline:
"From Concept to Capacity – Your Self Storage Experts"
• Subheadline: “Keelbrook Vault Holdings delivers turnkey design, construction, leasing, and management services for profitable self storage operations.”
• Quick Service Icons:
o Facility Design & Development
o Construction & Build Management
o Lease-Up & Marketing
o Ongoing Facility Management
• Call to Action Button: “LEARN MORE” → links to ABOUT US page.
• Featured Project Highlights: Showcase a few completed or current projects with photos and stats.
• Contact Banner: “Ready to build your next self storage project? Let’s talk.” → CONTACT page.
2. ABOUT US
Purpose: Build credibility, showcase experience, and explain the value proposition.
Content Highlights:
• Who We Are: Overview of Keelbrook Vault Holdings’ history, mission, and team expertise.
• Our Approach: End-to-end process from site selection to occupancy.
• Why Choose Us:
o Industry expertise in self storage
o Proven track record in lease-up success
o Strong vendor and contractor network
3. SERVICES
Purpose: Detail all service offerings with clarity and authority.
Sections:
• Design & Development: Market analysis, site planning, and architectural design.
• Construction Management: Overseeing timelines, budgets, and quality control.
• Lease-Up Strategy: Marketing, promotions, and occupancy acceleration.
• Ongoing Facility Management: Staffing, maintenance, revenue optimization.

4. CONTACT
Purpose: Provide simple, direct ways to connect.
Content Highlights:
• Contact Form (Name, Email, Phone, Message)
• Direct Email: info@keelbrookvault.net
• Phone (if applicable)
• Google Map embed (if there’s a head office location)
• CTA: “Let’s Build Your Storage Success Story.”
Design & Technical Notes
• Visual Style: Clean, modern, bold typography, professional color palette (to be based on branding), strong imagery of self storage facilities.
• Performance: Image compression, caching, responsive scaling.
• SEO Targets: “Self storage facility developer,” “self storage construction,” “self storage management company,” “lease-up services for self storage.”

WordPress or Joomla – must be desktop and mobile friendly with fast page load speed. Need the ability to edit ourselves.

Use pantone colours - #033c5a – dark blue
#2baadf – light blue

```html
<!DOCTYPE html>
<html lang="en">
<head>
<meta charset="utf-8">
<title>Contact Us – Keelbrook Vault Holdings</title>
<link href="https://fonts.googleapis.com/css2?family=Montserrat:wght@400;500;700&family=Poppins:wght@400;500;600;700&display=swap" rel="stylesheet">
<style>
:root{
  --navy:#033c5a;
  --sky:#2baadf;
  --ink:#2b3a44;
  --white:#ffffff;
  --line:#dfe3e6;
  --map:#c9cbcd;
}
*{margin:0;padding:0;box-sizing:border-box}
html,body{width:1200px;height:2458px;overflow:hidden;background:var(--white)}
body{position:relative;font-family:'Poppins',sans-serif;color:var(--navy)}
.abs{position:absolute}

/* header */
.site-header{left:0;top:0;width:1200px;height:90px;background:var(--white)}
.brand{left:85px;top:27px;display:flex;align-items:center;gap:10px}
.brand-mark{width:34px;height:34px;background:var(--navy)}
.brand-name{font-family:'Poppins',sans-serif;font-weight:600;font-size:19px;color:var(--navy);line-height:1}
.main-nav{left:668px;top:36px;display:flex;gap:27px;font-size:13.5px;font-weight:500;color:var(--navy)}
.main-nav .active{color:var(--sky);font-weight:600;border-bottom:3px solid var(--sky);padding:0 4px 6px}
.btn-learn{left:981px;top:26px;width:130px;height:39px;background:var(--sky);color:var(--white);font-size:12.5px;font-weight:600;display:flex;align-items:center;justify-content:center}

/* hero */
.hero{left:0;top:90px;width:1200px;height:437px;background:linear-gradient(100deg,#1d2a3a 0%,#2c5aa3 35%,#4d7fc4 55%,#2e2a25 75%,#4a3f34 100%)}
.hero-title{left:0;top:268px;width:1200px;text-align:center;font-family:'Montserrat',sans-serif;font-weight:700;font-size:54px;color:var(--white)}

/* intro */
.intro-mark{left:570px;top:600px;width:60px;height:60px;background:var(--navy)}
.intro-text{left:270px;top:683px;width:660px;text-align:center;font-family:'Montserrat',sans-serif;font-size:20.5px;line-height:27px;color:var(--navy)}

/* form */
.form-panel{left:113px;top:821px;width:458px;height:547px;background:var(--navy)}
.field-label{left:166px;font-size:11px;font-weight:700;color:var(--white)}
.field{left:166px;width:350px;height:43px;background:var(--white);font-size:11px;color:#6d7378;padding:13px 19px}
.field.message{height:100px}
.btn-send{left:166px;top:1281px;width:350px;height:43px;background:var(--sky);color:var(--white);font-size:13.5px;font-weight:700;display:flex;align-items:center;justify-content:center}
.btn-send svg{position:absolute;right:16px;top:13px}

/* contact info */
.touch-title{left:689px;top:860px;font-size:46px;font-weight:700;color:var(--navy)}
.info-icon{left:693px;width:80px;height:80px;background:var(--sky);display:flex;align-items:center;justify-content:center;box-shadow:0 10px 40px rgba(3,60,90,.08)}
.info-text{left:802px;font-size:18px;font-weight:600;line-height:23px;color:var(--navy)}
.info-rule{left:802px;width:309px;height:1px;background:var(--line)}

/* map */
.find-title{left:0;top:1458px;width:1200px;text-align:center;font-size:40px;font-weight:700;color:var(--navy)}
.find-sub{left:0;top:1522px;width:1200px;text-align:center;font-size:13px;color:var(--navy)}
.map-card{left:113px;top:1565px;width:975px;height:472px;background:var(--white);box-shadow:0 10px 40px rgba(0,0,0,.08)}
.map-area{left:125px;top:1573px;width:951px;height:454px;background:var(--map)}

/* footer */
.site-footer{left:0;top:2142px;width:1200px;height:316px;background:var(--navy)}
.footer-brand{left:95px;top:2278px;display:flex;align-items:center;gap:14px}
.footer-brand .brand-mark{width:46px;height:46px;background:var(--white)}
.footer-brand .brand-name{color:var(--white);font-size:34px}
.footer-nav{left:712px;top:2264px;display:flex;gap:38px;font-size:19px;font-weight:500;color:var(--white)}
.footer-nav .active{font-weight:700}
.social{top:2305px;width:30px;height:30px;border-radius:50%;background:rgba(255,255,255,.12)}
.footer-rule{left:75px;top:2404px;width:1050px;height:1px;background:rgba(255,255,255,.15)}
.copyright{left:0;top:2421px;width:1200px;text-align:center;font-size:15.5px;font-weight:500;color:var(--white)}
.to-top{left:1144px;top:2384px;width:40px;height:40px;border-radius:50%;background:var(--sky);display:flex;align-items:center;justify-content:center}
</style>
</head>
<body>

<header class="site-header abs">
  <div class="brand abs"><span class="brand-mark"></span><span class="brand-name">Keelbrook Vault Holdings</span></div>
  <nav class="main-nav abs"><span class="active">HOME</span><span>About Us</span><span>Services</span><span>Contact</span></nav>
  <a class="btn-learn abs">LEARN MORE</a>
</header>

<section class="hero abs" role="img" aria-label="Photo of modern office buildings against a clear blue sky"></section>
<h1 class="hero-title abs">Contact Us</h1>

<div class="intro-mark abs"></div>
<p class="intro-text abs">We’d love to hear from you! Whether you’re ready to start a new self storage project or have questions about our services, connecting with us is easy.</p>

<div class="form-panel abs"></div>
<div class="field-label abs" style="top:885px">NAME*</div>
<div class="field abs" style="top:905px">Enter your name</div>
<div class="field-label abs" style="top:964px">EMAIL*</div>
<div class="field abs" style="top:984px">Enter your email</div>
<div class="field-label abs" style="top:1043px">PHONE*</div>
<div class="field abs" style="top:1063px">Enter phone number</div>
<div class="field-label abs" style="top:1122px">MESSAGE*</div>
<div class="field message abs" style="top:1142px">Type your message</div>
<div class="btn-send abs">SEND MESSAGE
  <svg width="18" height="16" viewBox="0 0 18 16"><path d="M17 1 1 8l5 2 1 5 3-3 4 3z" fill="#fff"/></svg>
</div>

<h2 class="touch-title abs">Get in touch</h2>

<div class="info-icon abs" style="top:963px">
  <svg width="30" height="22" viewBox="0 0 30 22"><rect x="1" y="1" width="28" height="20" rx="2" fill="#fff"/><path d="M2 3l13 9 13-9" stroke="#2baadf" stroke-width="2.5" fill="none"/></svg>
</div>
<div class="info-text abs" style="top:985px">Email:<br>info@keelbrookvault.net</div>
<div class="info-rule abs" style="top:1064px"></div>

<div class="info-icon abs" style="top:1074px">
  <svg width="30" height="30" viewBox="0 0 24 24"><path d="M6.6 10.8a15 15 0 0 0 6.6 6.6l2.2-2.2c.3-.3.7-.4 1-.2 1.1.4 2.3.6 3.6.6.6 0 1 .4 1 1V20c0 .6-.4 1-1 1A17 17 0 0 1 3 4c0-.6.4-1 1-1h3.5c.6 0 1 .4 1 1 0 1.3.2 2.5.6 3.6.1.3 0 .7-.2 1z" fill="#fff"/></svg>
</div>
<div class="info-text abs" style="top:1093px">Phone:<br>+1-780-555-0142</div>
<div class="info-rule abs" style="top:1176px"></div>

<div class="info-icon abs" style="top:1187px">
  <svg width="24" height="32" viewBox="0 0 24 32"><path d="M12 0C5.4 0 0 5.2 0 11.7 0 20 12 32 12 32s12-12 12-20.3C24 5.2 18.6 0 12 0z" fill="#fff"/><circle cx="12" cy="11.5" r="4.5" fill="#2baadf"/></svg>
</div>
<div class="info-text abs" style="top:1203px">Address:<br>40837 52 Ave, Edmonton, AB T6K 3R8</div>

<h2 class="find-title abs">Find Us Keelbrook</h2>
<p class="find-sub abs">Visit our office or schedule a meeting to discuss your project in person.</p>
<div class="map-card abs"></div>
<div class="map-area abs" role="img" aria-label="Street map showing the head office location"></div>

<footer class="site-footer abs"></footer>
<div class="footer-brand abs"><span class="brand-mark"></span><span class="brand-name">Keelbrook Vault Holdings</span></div>
<nav class="footer-nav abs"><span class="active">HOME</span><span>About Us</span><span>Services</span><span>Contact</span></nav>
<span class="social abs" style="left:968px"></span>
<span class="social abs" style="left:1005px"></span>
<span class="social abs" style="left:1041px"></span>
<span class="social abs" style="left:1077px"></span>
<div class="footer-rule abs"></div>
<p class="copyright abs">© Copyright 2025. All Rights Reserved</p>
<a class="to-top abs" aria-label="Back to top">
  <svg width="10" height="6" viewBox="0 0 10 6"><path d="M1 5l4-4 4 4" stroke="#fff" stroke-width="1.6" fill="none"/></svg>
</a>

</body>
</html>
```